London Based Property Finding Company - have logo already

We find property for private purchasers and investors in London, UK.  We work for the BUYER, whereas estate agencies/real estate companies work for the seller. We offer a much more personalised service to UK and overseas purchasers.

We would like the following:

*A double sided business card

*A letterhead

We have attached two versions of the logo. Each logo style is set on two different coloured backgrounds. Please choose one of the two designs, whichever you prefer or feel more comfortable with, and produce one in black and one in white background.

This applies to both pieces of stationery.

THE BUSINESS CARD:

We would like the company name placed on its own on one side of the card and the contact details and what we do on the other.

e.g.

SIDE 1:

BRAMWELL PROPERTY FINDERS

SIDE 2:

Owen Bramwell

t: 0208 394 2860

m: +44(0)7932 418 507

e: info@bramwellpropertyfinders.co.uk

w: bramwellpropertyfinders.co.uk

London Property Finders and Search Agents

I will leave the layout up to you, but a minimalist layout is preferred. If you would like to put additional detial or design on the card then that is up to, but not specified.

It is optional to have the company name on side 2, but if you do use it, please make it smaller. than on the 1st side.

The design needs to be simple, professional and not too in your face.

If you are using the black background design on side 1 for the logo, then maybe a white backgounnd can be used on side 2 with a black typeface.

The type face for the contacts details should be sans serif standard typeface. Please experiment with the desciprtion.

-

THE LETTERHEAD;

You can experiment with the layout for the letterhead. e.g logo centre aligned on the top of the page with the contact details and address at the bottom of the page OR the logo, description running along a bar on the top of the page with the contact details and website address at the bottom. Please try and experiment with this, but the less 'busy', the better.

Here is info that needs to be on the letterhead.

Bramwell Property Finders

t: 0208 394 2860

m: +44(0)7932 418 507

(PLEASE NOTE; the below company info must be placed at the bottom of the page as a footer, in small text.)

Kestrand Holdings Ltd Trading as Bramwell Property Finders, a company registered in England & Wales, No.7351926 , Registered office is 41 Hollinmoor Court, Hollinmoor Road, London, SW9 3PL, t: 0208 394 2860, m: +44(0)7932 418 507, e: info@bramwellpropertyfinders.co.uk

Best of luck!

Thank you

Dear Designer,

I have now attached the supporting files to this brief.

Thanks,

Owen Bramwell
Bramwell Property Finders

```html
<!DOCTYPE html>
<html lang="en">
<head>
<meta charset="utf-8">
<title>Bramwell Property Finders — Stationery</title>
<link rel="stylesheet" href="https://fonts.googleapis.com/css2?family=Arimo:ital,wght@0,400;0,700;1,400&family=Inter:wght@700&display=swap">
<style>
  :root {
    --ink: #000000;
    --charcoal: #2b2b2b;
    --paper: #ffffff;
    --muted: #8a8a8a;
    --shadow: rgba(0, 0, 0, 0.28);
  }
  * { box-sizing: border-box; margin: 0; padding: 0; }
  html, body { width: 1200px; height: 982px; overflow: hidden; background: var(--paper); }
  body { position: relative; font-family: "Arimo", Arial, sans-serif; color: var(--ink); }

  /* Letterhead */
  .letterhead {
    position: absolute; left: 22px; top: 20px; width: 665px; height: 945px;
    background: var(--paper); box-shadow: 0 0 8px var(--shadow);
  }
  .letterhead .brand { position: absolute; left: 27px; top: 45px; }
  .brand-name { font-size: 21px; letter-spacing: 0.04em; line-height: 1; }
  .brand-sub { font-size: 11px; letter-spacing: 0.28em; line-height: 15px; margin-top: 16px; }
  .sidebar-contact {
    position: absolute; left: 27px; top: 212px;
    font-size: 8px; font-weight: 700; line-height: 12px; letter-spacing: -0.01em;
  }
  .subject {
    position: absolute; left: 202px; top: 43px;
    background: var(--ink); color: var(--paper);
    font-family: "Inter", Arial, sans-serif; font-weight: 700;
    font-size: 33px; letter-spacing: -0.045em; line-height: 55px; padding: 0 14px 0 12px;
  }
  .byline {
    position: absolute; left: 202px; top: 107px;
    font-size: 11px; font-style: italic; color: var(--muted); letter-spacing: -0.02em;
  }
  .letter-body { position: absolute; left: 202px; top: 128px; width: 430px; }
  .letter-body p {
    font-size: 13.4px; line-height: 19.6px; text-align: justify; hyphens: auto;
    letter-spacing: -0.015em; margin-bottom: 19.6px;
  }
  .footer-rule {
    position: absolute; left: 317px; top: 850px; width: 31px; height: 1px; background: var(--ink);
  }
  .footer {
    position: absolute; left: 0; right: 0; top: 866px; text-align: center;
    font-size: 9.4px; line-height: 12.8px; letter-spacing: -0.01em;
  }

  /* Business card — front */
  .card { position: absolute; width: 384px; height: 248px; box-shadow: 0 0 7px var(--shadow); }
  .card-front { left: 733px; top: 23px; background: var(--charcoal); color: var(--paper); text-align: center; }
  .card-front .front-name {
    position: absolute; left: 0; right: 0; top: 91px; font-size: 25px; letter-spacing: 0.05em;
  }
  .card-front .front-sub {
    position: absolute; left: 0; right: 0; top: 198px; font-size: 11px; letter-spacing: 0.32em;
  }

  /* Business card — back */
  .card-back { left: 733px; top: 317px; background: var(--paper); }
  .name-block {
    position: absolute; left: 0; top: 31px;
    font-family: "Inter", Arial, sans-serif; font-weight: 700; font-size: 40px; letter-spacing: -0.06em;
  }
  .name-line {
    display: table; background: var(--charcoal); color: var(--paper);
    line-height: 52px; padding: 0 12px 0 14px;
  }
  .name-line + .name-line { line-height: 58px; }
  .card-contact {
    position: absolute; left: 14px; top: 164px;
    font-size: 11.4px; font-weight: 700; line-height: 18px; letter-spacing: -0.04em;
  }
  .card-tagline {
    position: absolute; left: 14px; top: 216px;
    font-size: 11.4px; font-weight: 700; letter-spacing: -0.04em;
  }
</style>
</head>
<body>

<section class="letterhead" aria-label="Letterhead">
  <div class="brand">
    <div class="brand-name">BRAMWELL</div>
    <div class="brand-sub">property<br>finders</div>
  </div>

  <address class="sidebar-contact" style="font-style: normal;">
    Bramwell Property Finders<br>
    0208 394 2860<br>
    +44(0)7932 418 507<br>
    info@bramwellpropertyfinders.co.uk<br>
    bramwellpropertyfinders.co.uk
  </address>

  <h1 class="subject">Document Subject</h1>
  <p class="byline">From Bramwell Owen written on 17.01.2010</p>

  <div class="letter-body">
    <p>Lorem ipsum dolor sit amet, consectetur adipisicing elit, sed do eiusmod tempor incididunt ut labore et dolore magna aliqua. Ut enim ad minim veniam, quis nostrud exercitation ullamco laboris nisi ut aliquip ex ea commodo consequat. Duis aute irure dolor in reprehenderit in voluptate velit esse cillum dolore eu fugiat nulla pariatur. Excepteur sint occaecat cupidatat non proident, sunt in culpa qui officia deserunt mollit anim id est laborum.</p>
    <p>Sed ut perspiciatis unde omnis iste natus error sit voluptatem accusantium doloremque laudantium, totam rem aperiam, eaque ipsa quae ab illo inventore veritatis et quasi architecto beatae vitae dicta sunt explicabo. Nemo enim ipsam voluptatem quia voluptas sit aspernatur aut odit aut fugit, sed quia consequuntur magni dolores eos qui ratione voluptatem sequi nesciunt. Neque porro quisquam est, qui dolorem ipsum quia dolor sit amet, consectetur, adipisci velit, sed quia non numquam eius modi tempora incidunt ut labore et dolore magnam aliquam quaerat voluptatem. Ut enim ad minima veniam, quis nostrum exercitationem ullam corporis suscipit laboriosam, nisi ut aliquid ex ea commodi consequatur? Quis autem vel eum iure reprehenderit qui in ea voluptate velit esse quam nihil molestiae consequatur, vel illum qui dolorem eum fugiat quo voluptas nulla pariatur?</p>
  </div>

  <div class="footer-rule"></div>
  <footer class="footer">
    Kestrand Holdings Ltd Trading as Bramwell Property Finders<br>
    A company registered in England &amp; Wales<br>
    No.7351926 , Registered office is 41 Hollinmoor Court, Hollinmoor Road, London, SW9 3PL<br>
    t: 0208 394 2860, m: +44(0)7932 418 507, e: info@bramwellpropertyfinders.co.uk
  </footer>
</section>

<section class="card card-front" aria-label="Business card front">
  <div class="front-name">BRAMWELL</div>
  <div class="front-sub">property finders</div>
</section>

<section class="card card-back" aria-label="Business card back">
  <div class="name-block">
    <span class="name-line">Owen</span>
    <span class="name-line">Bramwell</span>
  </div>
  <p class="card-contact">
    0208 394 2860 / +44(0)7932 418 507<br>
    info@bramwellpropertyfinders.co.uk / bramwellpropertyfinders.co.uk
  </p>
  <p class="card-tagline">London Property Finders and Search Agents</p>
</section>

</body>
</html>
```